Industrial & commercial facility maintenance flyer

Design a 2 sided flyer that outlines our core business unit services. One side shall be for our industrial maintenance division while the other will be focused on our commercial maintenance division.

Media from website here: https://files.vornelbox.net/share/7Kq29XzPw4RtLmYc8NdHe5JbVa

Target Market(s)

Industrial and commercial facility maintenance companies and professionals

Industry/Entity Type

Maintenance

Font styles to use
Serif

Colors
ffffff
2f73b4
0455a3
cfdfed

Requirements
Must have
• Several photos of each applicable service. Reference existing website (www.trelcorp.com). Use of the blue and grey scheme of our current logo.
Nice to have
• Our logo design across the top with our contact information on the bottom.

```html
<!DOCTYPE html>
<html lang="en">
<head>
<meta charset="utf-8">
<title>Trelcor Maintenance Solutions – Service Flyers</title>
<link rel="stylesheet" href="https://fonts.googleapis.com/css2?family=Montserrat:wght@400;700&family=Questrial&family=Oswald:wght@400;500&family=Roboto+Condensed:wght@400;500&display=swap">
<style>
  :root{
    --blue:#0455a3;
    --blue-mid:#2f73b4;
    --blue-pale:#cfdfed;
    --white:#ffffff;
    --backdrop:#8e8d8e;
    --band:#ebebeb;
    --footer-grey:#58595b;
    --text:#2b2b2b;
  }
  *{box-sizing:border-box;margin:0;padding:0}
  html,body{width:1200px;height:1200px;overflow:hidden}
  body{background:var(--backdrop);position:relative;font-family:"Questrial",sans-serif;color:var(--text)}

  .flyer{position:absolute;top:196px;width:548px;height:770px;background:var(--white);
    box-shadow:0 6px 14px rgba(0,0,0,.35);overflow:hidden}
  .flyer--industrial{left:34px}
  .flyer--retail{left:618px}

  /* masthead */
  .masthead{position:absolute;top:0;left:0;width:100%;height:124px;display:flex;align-items:center;justify-content:center;gap:12px}
  .masthead__square{width:18px;height:18px;background:var(--blue);flex:none}
  .masthead__name{font-family:"Montserrat",sans-serif;font-weight:700;font-size:21px;color:var(--blue);line-height:1}

  /* hero */
  .hero{position:absolute;top:124px;left:0;width:548px;height:240px;
    clip-path:polygon(0 0,370px 0,410px 24px,548px 24px,548px 240px,145px 240px,102px 214px,0 214px)}
  .hero--industrial{background:linear-gradient(90deg,#2b3a55 0%,#4a5870 45%,#7b8592 75%,#4b5466 100%)}
  .hero--retail{background:linear-gradient(90deg,#28406c 0%,#34508a 40%,#5b6f8e 62%,#1f58b0 78%,#1a4fa3 100%)}
  .hero__title{position:absolute;left:22px;top:80px;font-family:"Montserrat",sans-serif;font-weight:700;
    font-size:25px;line-height:31px;color:var(--white);letter-spacing:.3px}

  /* intro band */
  .intro{position:absolute;top:375px;left:0;width:100%;height:105px;background:var(--band);padding:28px 32px 0 22px;
    font-size:10.6px;line-height:12.8px;text-align:justify}

  /* services */
  .services{position:absolute;top:480px;left:0;width:100%;height:228px}
  .services__heading{position:absolute;left:22px;top:22px;font-family:"Roboto Condensed",sans-serif;font-weight:500;
    font-size:16px;color:var(--blue)}
  .services__list{position:absolute;left:22px;top:45px;width:296px;list-style:none}
  .services__list li{position:relative;padding-left:11px;text-align:justify;font-size:9.4px;line-height:11.9px;margin-bottom:12px}
  .services__list li::before{content:"";position:absolute;left:0;top:2px;width:7px;height:7px;border:1px solid #666;border-radius:50%}
  .flyer--retail .services__list li{font-size:8.3px;line-height:10.8px;padding-left:12px}
  .services__photo{position:absolute;left:338px;top:14px;width:201px;height:200px;border:2px solid var(--blue)}
  .photo--plant{background:linear-gradient(160deg,#5d7186 0%,#3c6e9a 40%,#b8ac5a 70%,#8c9096 100%)}
  .photo--technician{background:linear-gradient(160deg,#e2e1dc 0%,#c9c8c2 40%,#2c56b2 65%,#d7d4cc 100%)}

  /* footer */
  .footer{position:absolute;left:0;bottom:0;width:100%;height:62px}
  .footer__grey{position:absolute;right:0;bottom:0;width:100%;height:44px;background:var(--footer-grey)}
  .footer__blue{position:absolute;left:0;bottom:0;width:294px;height:62px;background:var(--blue);
    clip-path:polygon(0 0,258px 0,294px 62px,0 62px);display:flex;align-items:center;padding-left:26px;gap:8px}
  .footer__phone{font-family:"Oswald",sans-serif;font-size:29px;color:var(--white);letter-spacing:-.5px;line-height:1}
  .footer__web{position:absolute;right:32px;bottom:14px;display:flex;align-items:center;gap:5px;
    font-family:"Montserrat",sans-serif;font-size:13px;letter-spacing:4.3px;color:var(--white)}
  .footer__web svg{flex:none}
</style>
</head>
<body>

<article class="flyer flyer--industrial">
  <header class="masthead">
    <span class="masthead__square"></span>
    <span class="masthead__name">Trelcor Maintenance Solutions</span>
  </header>

  <section class="hero hero--industrial" role="img" aria-label="Photo of an industrial plant with steel towers and pipework">
    <h1 class="hero__title">Industrial Maintenance<br>Solutions</h1>
  </section>

  <p class="intro">Our industrial maintenance teams work in the field to handle your needs as quickly as possible, whether to get your critical broken or malfunctioning equipment going again or to support scheduled downtime. We specialize in industrial maintenance, conveyer repair, and overhead door repair, but our industrial services aren't limited to those services. Others include equipment repairs, installation, and adjustment, just to name a few.</p>

  <section class="services">
    <h2 class="services__heading">What we Provide</h2>
    <ul class="services__list">
      <li>Trelcor Maintenance Solutions has been Atlanta's trusted industrial and commercial maintenance solution for over 10 years. Our industrial teams are available 24/7 for equipment maintenance, installation, or repair, and can be onsite within 4 hours.</li>
      <li>We provide conveyor system repair and overhead door repair and maintenance, but our services don't end there. We cater to your needs to provide exactly what services you want. Other services we offer include plant maintenance, equipment installation and relocation, and repairs of all types of process and manufacturing equipment. In addition to the physical element of industrial maintenance, we also offer facility safety consultations.</li>
    </ul>
    <div class="services__photo photo--plant" role="img" aria-label="Photo of a factory floor with a roller conveyor line"></div>
  </section>

  <footer class="footer">
    <div class="footer__grey"></div>
    <div class="footer__blue">
      <svg width="24" height="24" viewBox="0 0 24 24" aria-hidden="true"><path d="M6 3l3 4-2 2c1 3 4 6 7 7l2-2 4 3-2 3c-7 0-15-8-15-15z" fill="#fff"/><path d="M14 4a6 6 0 0 1 6 6M14 7a3 3 0 0 1 3 3" stroke="#fff" stroke-width="1.6" fill="none"/></svg>
      <span class="footer__phone">00321 654 987</span>
    </div>
    <div class="footer__web">
      <svg width="9" height="9" viewBox="0 0 10 10" aria-hidden="true"><circle cx="5" cy="5" r="4" fill="none" stroke="#fff" stroke-width="1.4"/><path d="M1 5h8M5 1v8" stroke="#fff" stroke-width="1"/></svg>
      <span>www.trelcorp.com</span>
    </div>
  </footer>
</article>

<article class="flyer flyer--retail">
  <header class="masthead">
    <span class="masthead__square"></span>
    <span class="masthead__name">Trelcor Maintenance Solutions</span>
  </header>

  <section class="hero hero--retail" role="img" aria-label="Photo of a city skyline beside a worker's arm holding a wrench">
    <h1 class="hero__title">Retail &amp; Commercial<br>Maintenance Solutions</h1>
  </section>

  <p class="intro">Trelcor Maintenance Solutions knows how important it is to convert window shoppers to paying customers and to move inventory off your shelves. We ensure that your business is always looking its best with our cost-effective maintenance programs and crews available 24/7 to take care of any equipment or facility malfunction as quickly as possible.</p>

  <section class="services">
    <h2 class="services__heading">What we Provide</h2>
    <ul class="services__list">
      <li>Trelcor Maintenance Solutions provides services to stand-alone stores and big box stores alike, malls, nightclubs, and more. We work to enhance your image by taking preventative measures, like inspecting equipment for signs of wear or failing components. We service equipment as needed, measuring either by usage or manufacturer recommendations. After maintenance and repairs, our technicians provide an in-depth report on equipment conditions, analyze equipment failure, and discuss future prevention.</li>
      <li>Customers may not realize how much work and effort goes into maintaining a functional well-kept business, but Trelcor Maintenance does. For your convenience, we offer a vast range of services to handle any issues that may occur or to help you expand your business, whether adding on to your existing location or moving to a new one.</li>
    </ul>
    <div class="services__photo photo--technician" role="img" aria-label="Photo of a technician in blue overalls with a tool belt and toolbox beside a van"></div>
  </section>

  <footer class="footer">
    <div class="footer__grey"></div>
    <div class="footer__blue">
      <svg width="24" height="24" viewBox="0 0 24 24" aria-hidden="true"><path d="M6 3l3 4-2 2c1 3 4 6 7 7l2-2 4 3-2 3c-7 0-15-8-15-15z" fill="#fff"/><path d="M14 4a6 6 0 0 1 6 6M14 7a3 3 0 0 1 3 3" stroke="#fff" stroke-width="1.6" fill="none"/></svg>
      <span class="footer__phone">00321 654 987</span>
    </div>
    <div class="footer__web">
      <svg width="9" height="9" viewBox="0 0 10 10" aria-hidden="true"><circle cx="5" cy="5" r="4" fill="none" stroke="#fff" stroke-width="1.4"/><path d="M1 5h8M5 1v8" stroke="#fff" stroke-width="1"/></svg>
      <span>www.trelcorp.com</span>
    </div>
  </footer>
</article>

</body>
</html>
```